Product Label Design for Natural Cosmetics brand

For our company Solmirena, we are looking for a completely new label design for our natural cosmetics line made with Organic Aloe Vera.
The first product in line is Travessa, our Aloe Vera Gel. Based on the schema you create, further labels would have to be created.
Since the line includes different products (for Face, Body, Hands, Sun), there should be some color distinction between different product that can keep the products apart, having still a very similar schema.
The label should reflect the South Portuguese (Algarve) way, trust and quality. The label design should be minimalistic, well recognizable and readable, including though the following components
Logo
Product Name: Travessa (medium)
Product Function (in Portuguese mainly): GEL DE ALOÉ VERA BIO (Large and visible)
Key Infomation: For Skin and Hair
Contains 200x concentrated Aloe Vera and Organic Jojoba Oil
Following logos are to be placed on the packaging: Vegan, Organic Aloe Vera, Natural Product
Additional Info:
Barcode (EAN Number)
Ingredients (please see the current label)
Made in Portugal
Address: Check current label
QR Code for URL to open Instructions and get support
Functions and Instructions need to be in the following language:
Function: Bio Aloe Vera Gel
Instruction: External Use.
English, Spanish, French, Italian, German, Dutch, Swedish, Portuguese, Arabic
Please use google translate or put placeholders for the respective languages.
I am uploading the current label (content and design is different than what we are looking for), the package (the amber pump bottle remains the same and is available to see at https://solmirena.example/default/travessa-aloe-vera-gel-1.html ) and the logo.
We would like you to illustrate how the label would look on the bottle and how you plan to distinct between other products that we will be designing in the series.
Please let me know if you need anything else.

```html
<!DOCTYPE html>
<html lang="pt">
<head>
<meta charset="utf-8">
<title>Solmirena Travessa – Gel de Aloé Vera Bio labels</title>
<link rel="stylesheet" href="https://fonts.googleapis.com/css2?family=Arimo:wght@400&family=Montserrat:wght@400;600;700&family=Quicksand:wght@500;600;700&display=swap">
<style>
:root{
  --page:#ffffff;
  --ink:#1f1f1f;
  --navy:#2e3347;
  --white:#ffffff;
  --green-dark:#3f8b3f;
  --green-light:#74b864;
  --yellow-dark:#f1c22e;
  --yellow-light:#fbe27a;
  --badge-green:#e8f3e3;
  --badge-yellow:#2e3347;
}
*{margin:0;padding:0;box-sizing:border-box}
html,body{width:849px;height:1200px;overflow:hidden;background:var(--page)}
body{position:relative;font-family:"Montserrat",sans-serif;color:var(--ink)}
.variant-title{position:absolute;left:40px;font-family:"Arimo",sans-serif;font-size:14px}
.variant-title--body{top:51px}
.variant-title--face{top:608px}

.label{position:absolute;left:40px;width:762px;height:296px;overflow:hidden}
.label--body{top:76px;--fg:var(--white);--small:var(--white);--badge:var(--badge-green)}
.label--face{top:634px;--fg:var(--navy);--small:var(--navy);--badge:var(--badge-yellow)}
.label__backdrop{position:absolute;inset:0}
.label--body .label__backdrop{background:radial-gradient(ellipse at 70% 30%,var(--green-light),var(--green-dark) 75%)}
.label--face .label__backdrop{background:radial-gradient(ellipse at 65% 25%,var(--yellow-light),var(--yellow-dark) 75%)}

.languages{position:absolute;left:62px;top:50px;font-size:6.5px;line-height:9px;color:var(--small)}
.ingredients{position:absolute;left:30px;top:96px;width:205px;font-size:6.8px;line-height:10px;font-weight:600;color:var(--small)}
.made-in{position:absolute;left:30px;top:165px;width:200px;text-align:center;font-size:6.5px;line-height:9px;color:var(--small)}
b{font-weight:700}
.barcode-area{position:absolute;left:29px;top:217px;width:108px;height:60px;background:var(--white)}
.volume{position:absolute;left:145px;top:222px;font-family:"Quicksand",sans-serif;font-weight:600;font-size:20px;color:var(--fg)}
.volume span{font-size:26px}
.usage{position:absolute;left:146px;top:256px;width:90px;font-size:4.5px;line-height:6px;color:var(--small)}

.brand-mark{position:absolute;left:315px;top:-6px;width:130px;height:110px}
.brand-mark__name{position:absolute;left:0;top:0;width:130px;height:110px;display:flex;align-items:center;justify-content:center;font-family:"Quicksand",sans-serif;font-weight:700;font-size:11px;letter-spacing:1.5px;color:var(--green-dark)}

.product-name{position:absolute;left:298px;top:130px;font-family:"Quicksand",sans-serif;font-weight:600;font-size:16px;letter-spacing:.5px;color:var(--fg)}
.product-function{position:absolute;left:298px;top:148px;font-family:"Quicksand",sans-serif;font-weight:700;font-size:25px;line-height:29px;color:var(--fg)}
.product-use{position:absolute;left:298px;top:207px;font-family:"Quicksand",sans-serif;font-weight:500;font-size:11px;color:var(--fg)}
.key-claim{position:absolute;left:255px;top:235px;width:240px;height:41px;border-radius:12px;background:var(--white);display:flex;align-items:center;justify-content:center;text-align:center;font-family:"Quicksand",sans-serif;font-weight:600;font-size:11px;line-height:14px;color:var(--ink)}

.story{position:absolute;left:530px;top:148px;width:200px;text-align:center;font-family:"Quicksand",sans-serif;font-weight:600;font-size:11px;line-height:14px;color:var(--white)}
.badges{position:absolute;left:548px;top:228px;display:flex;gap:42px;align-items:center}
.badge{width:34px;height:34px;border-radius:50%;background:var(--badge)}
.badge--wide{width:46px;height:28px;border-radius:14px 4px 14px 4px}
</style>
</head>
<body>

<p class="variant-title variant-title--body">Corpo</p>
<section class="label label--body">
  <div class="label__backdrop" role="img" aria-label="Soft green background with blurred aloe leaves"></div>
  <p class="languages"><b>ES</b> Gel de Aloe Vera <b>NL</b> Aloe Vera Gel<br><b>DE</b> Aloe Vera Gel <b>FR</b> Gel d'Aloe Vera</p>
  <p class="ingredients"><b>INGREDIENTES:</b> Aqua, Aloe Barbadensis Leaf Water, Glycerin, Alcohol, Xanthan Gum, Simmondsia Chinensis Seed Oil, Aloe Barbadensis Leaf Powder, Sodium, Hyaluronate, Tocopherol, Potassium Sorbate, Benzoic Acid, Organic.</p>
  <p class="made-in"><b>MADE IN PORTUGAL</b> | Solmirena Lda.<br>Rua das Figueiras, 12, 8800-000 - Tavira<br>www.solmirena.example</p>
  <div class="barcode-area"></div>
  <p class="volume">300ml<span>e</span></p>
  <p class="usage">Application: external use only.<br>Aplicação: apenas uso externo.</p>
  <div class="brand-mark">
    <svg width="130" height="110" viewBox="0 0 130 110" aria-hidden="true">
      <path d="M18 40 C20 10 60 0 90 8 C120 16 128 50 112 76 C96 104 50 110 28 90 C12 76 16 58 18 40Z" fill="#fff"/>
    </svg>
    <span class="brand-mark__name">SOLMIRENA</span>
  </div>
  <p class="product-name">TRAVESSA</p>
  <h1 class="product-function">GEL DE ALOÉ<br>VERA BIO</h1>
  <p class="product-use">Para pele e cabelo</p>
  <p class="key-claim">Contém 200x concentrado de Aloe<br>Vera e Óleo de Jojoba Orgânico</p>
  <p class="story">"Travessa" means "Crossing".<br>Immerse your whole body in this gel made with organic water from aloe vera and organic jojoba oil, and feel the difference.</p>
  <div class="badges"><span class="badge"></span><span class="badge badge--wide"></span><span class="badge"></span></div>
</section>

<p class="variant-title variant-title--face">Rosto</p>
<section class="label label--face">
  <div class="label__backdrop" role="img" aria-label="Soft yellow background with sunlit blurred leaves"></div>
  <p class="languages"><b>ES</b> Gel de Aloe Vera <b>NL</b> Aloe Vera Gel<br><b>DE</b> Aloe Vera Gel <b>FR</b> Gel d'Aloe Vera</p>
  <p class="ingredients"><b>INGREDIENTES:</b> Aqua, Aloe Barbadensis Leaf Water, Glycerin, Alcohol, Xanthan Gum, Simmondsia Chinensis Seed Oil, Aloe Barbadensis Leaf Powder, Sodium, Hyaluronate, Tocopherol, Potassium Sorbate, Benzoic Acid, Organic.</p>
  <p class="made-in"><b>MADE IN PORTUGAL</b> | Solmirena Lda.<br>Rua das Figueiras, 12, 8800-000 - Tavira<br>www.solmirena.example</p>
  <div class="barcode-area"></div>
  <p class="volume">300ml<span>e</span></p>
  <p class="usage">Application: external use only.<br>Aplicação: apenas uso externo.</p>
  <div class="brand-mark">
    <svg width="130" height="110" viewBox="0 0 130 110" aria-hidden="true">
      <path d="M18 40 C20 10 60 0 90 8 C120 16 128 50 112 76 C96 104 50 110 28 90 C12 76 16 58 18 40Z" fill="#fff"/>
    </svg>
    <span class="brand-mark__name">SOLMIRENA</span>
  </div>
  <p class="product-name">TRAVESSA</p>
  <h2 class="product-function">GEL DE ALOÉ<br>VERA BIO</h2>
  <p class="product-use">Para pele e cabelo</p>
  <p class="key-claim">Contém 200x concentrado de Aloe<br>Vera e Óleo de Jojoba Orgânico</p>
  <p class="story">"Travessa" means "Crossing".<br>Immerse your whole body in this gel made with organic water from aloe vera and organic jojoba oil, and feel the difference.</p>
  <div class="badges"><span class="badge"></span><span class="badge badge--wide"></span><span class="badge"></span></div>
</section>

</body>
</html>
```